Quiet Compass: Mapping a Calmer Working Week Book Cover

This book is titled, "Quiet Compass: Mapping a Calmer Working Week." It would be of the same size as QRT and will run to about 200 pages.
Here is a description to go on the back cover, which will give you some idea of the book's contents and value:
"The world we work in has now changed: it's more Volatile, Uncertain, Complex and Ambiguous (VUCA), and most of us are still engaging with our work in old ways. The VUCA world of work has crept up on most of us. As a result, many are suffering from time poverty, distraction and weariness, all leading to a sense of hopelessness. It is becoming overwhelming.
This book sets out a new emergent way of working which helps us all not merely to just get by, but to prosper and grow. We don't need to work faster, bigger, cheaper; we can simply choose to change the way we engage with our work."
In terms of the book structure, it is divided into two major parts:
A. The Physics of Self-Leadership. This covers margins, space, time and energy, the major dimensions with which knowledge workers manage their lives. This is the visible area where we can get "quick wins" of productivity.
B. The Soul of Self-Leadership, covering one's Identity, Presence, Destiny, and handling Relationships. These aspects of the soul, if shaped well, provide a more sustained, free life leadership.
You will find a couple of graphics I'm using within the book.
Updates

The background should be white, in the style of the cover I uploaded. One of the visual messages should be a life that is clean and uncluttered.Also, please no stock photography. Added Wednesday, August 31, 2016

Target Market(s)

Primarily for people leading change of all kinds, Programme Managers, Project Managers and Change Managers, who are overwhelmed, time poor, and distracted.

Font styles to use
Sans Serif

Colors
ffffff

Requirements
Must have
• Design in Adobe InDesign or Illustrator. I'm looking for a clean, modern look.
• The ISBN for the book will be 978-0-5518302-7-4 so the barcode on the back cover should be designed accordingly.
• The book synopsis (above in Project Description) should be on the back cover along with space for two or three short quotes.
• The overall effect should be fresh and positive.
Nice to have
• My previous book cover (see the upload) worked well. I'd like something in this house style. The fresh and positive sense could be around the concept of "freedom."
• As an example, I've uploaded an example cover that I admire: Tobias Fernhart's Brightmarking.
• In the subtitle, the word "Succeeding" is a strong one. I'd like it to be emphasised somehow.
• Also, the cover should imply positive, hopeful anticipation. I've added some illustrative graphics (stock photography from Pixavane) to give you an idea.
Should not have
• Please, no corney stock photography, particularly men in suits.

```html
<!DOCTYPE html>
<html lang="en">
<head>
<meta charset="utf-8">
<title>Quiet Compass – Book Cover</title>
<link rel="stylesheet" href="https://fonts.googleapis.com/css2?family=Poppins:wght@700&family=Arimo:wght@400;700&display=swap">
<style>
  :root {
    --stage: #000000;
    --paper: #ffffff;
    --brand-red: #ad1927;
    --ink: #111111;
    --sky: #a9d8f0;
    --sun: #f6e84a;
    --amber: #ef7d2e;
    --charcoal: #1c1c1c;
  }
  * { margin: 0; padding: 0; box-sizing: border-box; }
  html, body {
    width: 1200px;
    height: 999px;
    overflow: hidden;
    background: var(--stage);
  }
  .canvas {
    position: relative;
    width: 1200px;
    height: 999px;
    background: var(--stage);
  }
  .back-cover {
    position: absolute;
    left: 36px;
    top: 166px;
    width: 598px;
    height: 718px;
    background: var(--paper);
  }
  .synopsis {
    position: absolute;
    left: 83px;
    top: 48px;
    width: 356px;
    font-family: "Arimo", Arial, sans-serif;
    font-size: 14.6px;
    line-height: 19px;
    color: var(--ink);
    text-align: justify;
  }
  .synopsis p + p { margin-top: 19px; }
  .spine-title {
    position: absolute;
    left: 598px;
    top: 525px;
    transform: translate(-50%, -50%) rotate(-90deg);
    white-space: nowrap;
    font-family: "Poppins", sans-serif;
    font-weight: 700;
    font-size: 46px;
    letter-spacing: 0.5px;
    color: var(--brand-red);
    line-height: 1;
  }
  .front-cover {
    position: absolute;
    left: 634px;
    top: 166px;
    width: 527px;
    height: 718px;
    background: var(--paper);
    border-left: 1px solid #cfcfcf;
  }
  .title {
    position: absolute;
    left: 0;
    top: 16px;
    width: 527px;
    text-align: center;
    font-family: "Poppins", sans-serif;
    font-weight: 700;
    color: var(--brand-red);
    line-height: 1;
  }
  .title-main {
    display: block;
    font-size: 128px;
    letter-spacing: 1px;
  }
  .title-second {
    display: block;
    font-size: 82px;
    margin-top: 2px;
    letter-spacing: 1px;
  }
  .icon-cluster {
    position: absolute;
    left: 16px;
    top: 312px;
    width: 496px;
    height: 276px;
    border-radius: 40px;
    background: radial-gradient(ellipse at 50% 45%, rgba(246,232,74,0.35) 0%, rgba(169,216,240,0.35) 45%, rgba(255,255,255,0) 75%);
  }
  .subtitle-band {
    position: absolute;
    left: 0;
    top: 654px;
    width: 527px;
    height: 33px;
    background: var(--brand-red);
    display: flex;
    align-items: center;
    justify-content: center;
    font-family: "Arimo", Arial, sans-serif;
    font-weight: 700;
    font-size: 23px;
    color: var(--paper);
  }
</style>
</head>
<body>
<div class="canvas">
  <section class="back-cover">
    <div class="synopsis">
      <p>The world we work in has now changed: it's more Volatile, Uncertain, Complex and Ambiguous (VUCA), and most of us are still engaging with our work in old ways. The VUCA world of work has crept up on most of us. As a result, many are suffering from time poverty, distraction and weariness, all leading to a sense of hopelessness. It is becoming overwhelming.</p>
      <p>This book sets out a new emergent way of working which helps us all not merely to just get by, but to prosper and grow. We don't need to work faster, bigger, cheaper; we can simply choose to change the way we engage with our work.</p>
    </div>
  </section>

  <div class="spine-title">QUIET COMPASS</div>

  <section class="front-cover">
    <h1 class="title">
      <span class="title-main">QUIET</span>
      <span class="title-second">COMPASS</span>
    </h1>
    <div class="icon-cluster" role="img" aria-label="Cluster of small flat work icons around a central light bulb: clouds, gears, charts, calculator, briefcase, clock and money symbols in black, sky blue, yellow and orange"></div>
    <div class="subtitle-band">Mapping a Calmer Working Week</div>
  </section>
</div>
</body>
</html>
```